company, product, services, opportunity presentation

Lumivanta is a Payment Services Processor with value added product and services. We are focusing on the Payment Industry, Retail Merchants and Financial institutions. We have built total solution on QMO cloud to provide API based payment solutions such as Issuing of cards, Acquiring of payment transactions, Fraud prevention, Ecommerce, with customer facing APPs to provide dynamic virtual payment , 2FA and Passwordless sign in. Our focus is B2B .
We are developing our sales/investor pitch deck with slides covering company information, Market challengers (problems) that we are solving , Opportunities in the regional markets as well as global addressable Market for Payment cards. Lumivanta Product and services offerings to meet these challenges and opportunities.
Total Addressable Market statistics and data. Specific to virtual payment cards, Second factor authentication and digital ID (passwordless). Primarily data and justification for reducing Ecommerce card abandonment and increasing Authorization rates
Lumivanta Team and advisors’ slide. Current pipeline and customers. Use cases or case studies. Highlighting competitive advantage and USP. target clients and current pipline. Financials and projected spend in the next 2 years including target amount to raise fund. Solution and services slides and timeine of activities /roadmap
We need a PPT design to project better look and feel, crisp and eye catching graphic and design of the slides. clearer representation of key or salient points in all slides and information.

Target Market(s)

Financial Institutions, Retail (Merchants), Fintechs, Transportation

Industry/Entity Type

Cards and Payments Industry . Fraud prevention . Digital ID

Font styles to use
Sans Serif

Colors
F0912C
F2A743
F7CA91
FBE8D2
FDF5EE
EE7325
F08F49
F5BC92
FAE3D3
FDF4ED
A7469A
B969AE
D3A5CF
EDDBEB
F8F0F9
6B429C
8869AF
B7A5CE
E3DAEB
F3F0F8

Requirements
Must have
• problem to be solved, market challenges, market opportunities, product features and functionality. Use cases, Financial spend and funding. Team members and advisors. Timeline of roadmap for 2 years. competitive advantage and USP. Benefits to each customer segments
Nice to have
• Provision for future development on product and services. potentially covering other target markets such as Airlines, Insurance

```html
<!DOCTYPE html>
<html lang="en">
<head>
<meta charset="utf-8">
<title>Lumivanta – Pitch Deck Overview</title>
<link href="https://fonts.googleapis.com/css2?family=Poppins:wght@300;400;600;700&family=Open+Sans:wght@400;600&display=swap" rel="stylesheet">
<style>
:root{
  --purple:#7e2d86;
  --purple-soft:#a7469a;
  --purple-pale:#edd8eb;
  --lavender:#e3daeb;
  --lavender-mid:#b7a5ce;
  --orange:#ee8a2a;
  --orange-soft:#f2a743;
  --orange-pale:#fbe8d2;
  --ink:#3a3a3a;
  --muted:#8a8a8a;
  --board:#a6a6a6;
  --white:#ffffff;
}
*{margin:0;padding:0;box-sizing:border-box}
html,body{width:762px;height:1200px;overflow:hidden}
body{background:var(--board);position:relative;font-family:"Poppins",sans-serif;color:var(--ink)}
.slide{position:absolute;background:var(--white);overflow:hidden;box-shadow:2px 3px 5px rgba(0,0,0,.28)}
.small{width:215px;height:121px}
.abs{position:absolute}
.ring{position:absolute;border-radius:50%;border-style:solid}
.ring.purple{border-color:var(--purple)}
.ring.orange{border-color:var(--orange)}
.sq{position:absolute}
.sq.purple{background:var(--purple)}
.sq.orange{background:var(--orange)}
.photo{position:absolute}
.photo.mono-light{background:radial-gradient(ellipse at 65% 60%,#3c3c3c 0%,#6e6e6e 30%,transparent 55%),linear-gradient(160deg,#e4e4e4 0%,#b4b4b4 40%,#7a7a7a 75%,#444 100%)}
.photo.mono{background:radial-gradient(ellipse at 55% 45%,#d6d6d6 0%,transparent 50%),linear-gradient(140deg,#9a9a9a,#3d3d3d)}
.photo.warm{background:radial-gradient(ellipse at 40% 30%,#c79a7a 0%,transparent 45%),linear-gradient(135deg,#a89484 0%,#6d5b50 55%,#2e2a28 100%)}
.photo.cool{background:radial-gradient(ellipse at 60% 65%,#d2b49c 0%,transparent 40%),linear-gradient(135deg,#c9d4de 0%,#7f8c99 55%,#3b3f46 100%)}
.photo.dark{background:radial-gradient(ellipse at 30% 40%,#3a3438 0%,transparent 55%),linear-gradient(135deg,#262225,#0c0b0c)}
.body{position:absolute;font-family:"Open Sans",sans-serif;font-size:2.6px;line-height:3.5px;color:var(--muted)}
.label{position:absolute;font-weight:700;font-size:3.6px;color:var(--orange);letter-spacing:.1px}
.title-light{position:absolute;font-weight:300;color:var(--purple);line-height:1.05;text-transform:uppercase}
.title-bold{position:absolute;font-weight:700;color:var(--purple);line-height:1.05;text-transform:uppercase}
.foot{position:absolute;right:4px;bottom:6px;font-weight:700;font-size:5.5px;color:var(--purple);display:flex;align-items:center;gap:2px}
.foot .num{background:var(--orange);color:var(--white);font-size:3.6px;padding:0 1.5px;line-height:5px}
.foot.light{color:var(--white)}
.icon{position:absolute;border-radius:50%;background:var(--orange);border:1px solid var(--white);box-shadow:0 0 0 .6px var(--orange)}
.icon::after{content:"";position:absolute;left:30%;top:28%;width:40%;height:44%;border:.7px solid var(--white);border-radius:1px}

.cover{left:42px;top:66px;width:677px;height:381px}
.cover .photo{left:254px;top:0;width:423px;height:381px}
.cover .panel{position:absolute;left:110px;top:127px;width:283px;height:126px;background:var(--white)}
.cover .bar{position:absolute;left:110px;top:127px;width:18px;height:126px;background:var(--purple)}
.wordmark{position:absolute;left:155px;top:140px;font-weight:700;font-size:40px;color:var(--purple);letter-spacing:-.5px}
.tagline{position:absolute;left:160px;top:198px;font-family:"Open Sans",sans-serif;font-size:11px;line-height:15px;color:var(--orange)}
.tagline .first{color:#d7731f}
.site{position:absolute;left:27px;top:350px;font-size:11px;letter-spacing:4.5px;color:var(--purple)}

.contents-label{position:absolute;left:69px;top:48px;width:56px;height:24px;background:var(--white);font-weight:600;font-size:8px;color:var(--purple);padding:5px 0 0 9px}
.toc-item{position:absolute;left:128px;width:72px}
.toc-item b{display:block;font-size:3.6px;color:var(--orange)}
.toc-item span{display:block;font-family:"Open Sans",sans-serif;font-size:2.4px;line-height:3.2px;color:var(--muted)}

.part-num{position:absolute;left:45px;top:43px;width:43px;height:39px;background:var(--purple);color:var(--white);font-weight:700;font-size:16px;display:flex;align-items:center;justify-content:center}
.part-box{position:absolute;left:88px;top:43px;width:94px;height:39px;background:var(--white);padding:7px 6px}
.part-box h3{font-size:10px;font-weight:700;color:var(--purple);line-height:1}

.avatar{position:absolute;width:11px;height:11px;border-radius:50%;background:linear-gradient(135deg,#e6d9d0,#9b8a80)}
.org{position:absolute;border-radius:50%;background:linear-gradient(135deg,#d7c7bd,#8d7a70)}
.org.p{box-shadow:0 0 0 1.2px var(--purple)}
.org.o{box-shadow:0 0 0 1.2px var(--orange)}
.letter{position:absolute;font-size:4.5px;font-weight:600;color:#555}

.road-art{position:absolute;left:40px;top:10px;width:140px;height:88px;border-radius:44px 10px 44px 10px;background:linear-gradient(150deg,var(--lavender) 0%,var(--lavender-mid) 45%,#6b429c 100%)}
.opt{position:absolute;font-weight:600;font-size:3px;color:var(--purple)}
.opt span{display:block;font-family:"Open Sans",sans-serif;font-weight:400;font-size:1.9px;color:var(--muted)}

.grid-table{position:absolute;left:126px;top:26px;width:74px;border-collapse:collapse}
.grid-table td{border:.5px solid var(--white);background:var(--purple-pale);height:5.5px;font-size:1.6px;color:var(--purple);text-align:center}
.grid-table tr:first-child td{background:var(--purple);color:var(--white)}
.solutions-band{position:absolute;left:0;top:81px;width:193px;height:23px;background:var(--orange);color:var(--white);text-align:center;font-size:2.4px;line-height:3.2px;padding-top:2.5px}
.solutions-band b{display:block;font-size:2.6px}

.eco-head{position:absolute;left:10px;top:2px;width:205px;height:15px;background:var(--purple);color:var(--white);font-size:10px;padding-left:2px;line-height:15px;letter-spacing:.2px}
.eco-art{position:absolute;left:22px;top:22px;width:186px;height:92px;background:linear-gradient(120deg,#f3f0f8 0%,#fdf5ee 55%,#fbe8d2 100%);border-radius:4px}
</style>
</head>
<body>

<section class="slide cover">
  <div class="ring purple" style="left:-98px;top:-98px;width:196px;height:196px;border-width:12px"></div>
  <div class="photo mono-light" role="img" aria-label="Black and white photo of a hand holding a smartphone showing a payment success screen in front of a laptop"></div>
  <div class="sq purple" style="left:613px;top:26px;width:35px;height:34px"></div>
  <div class="panel"></div>
  <div class="bar"></div>
  <div class="wordmark">Lumivanta</div>
  <p class="tagline"><span class="first">online payment security</span><br>to eliminate cart abandonment</p>
  <div class="ring orange" style="left:185px;top:281px;width:170px;height:170px;border-width:21px;opacity:.92"></div>
  <div class="site">lumivanta.io</div>
</section>

<section class="slide small" style="left:42px;top:466px">
  <div class="photo warm" style="left:7px;top:7px;width:100px;height:106px" role="img" aria-label="Photo of a customer paying with a phone at a card terminal"></div>
  <div class="ring purple" style="left:-14px;top:92px;width:40px;height:40px;border-width:4px"></div>
  <div class="sq purple" style="left:92px;top:10px;width:11px;height:11px"></div>
  <div class="contents-label">Contents</div>
  <div class="toc-item" style="top:30px"><b>Company</b><span>Who we are, our cloud platform and<br>the payment services we provide today</span></div>
  <div class="toc-item" style="top:47px"><b>Market</b><span>Challenges, regional opportunity and<br>the addressable market for cards</span></div>
  <div class="toc-item" style="top:65px"><b>Product</b><span>Virtual cards, 2FA and passwordless<br>sign in for merchants and issuers</span></div>
  <div class="toc-item" style="top:82px"><b>Funding</b><span>Pipeline, two year roadmap, spend<br>plan and the amount we aim to raise</span></div>
  <div class="sq orange" style="left:205px;top:42px;width:10px;height:37px"></div>
  <div class="foot">Lumivanta <span class="num">02</span></div>
</section>

<section class="slide small" style="left:273px;top:466px">
  <div class="photo dark" style="left:0;top:0;width:215px;height:121px" role="img" aria-label="Dark photo of a person using a phone at a desk"></div>
  <div class="part-num">01.</div>
  <div class="part-box"><h3>Part One.</h3><p class="body" style="position:static;margin-top:2px">Company overview, the market we serve and the gap our payment platform closes.</p></div>
  <div class="sq purple" style="left:173px;top:43px;width:8px;height:8px"></div>
  <div class="foot light">Lumivanta <span class="num">03</span></div>
</section>

<section class="slide small" style="left:505px;top:466px">
  <div class="abs" style="left:0;top:0;width:215px;height:47px;background:#e9e9ec"></div>
  <div class="title-bold" style="left:12px;top:9px;font-size:7px">Problem to be<br>solved</div>
  <p class="body" style="left:12px;top:26px;width:80px">Shoppers drop carts when checkout asks for card data and codes. Declines and fraud checks cut approval rates for merchants and issuers alike.</p>
  <div class="photo mono" style="left:130px;top:20px;width:73px;height:84px" role="img" aria-label="Close-up photo of a payment card chip"></div>
  <div class="ring purple" style="left:152px;top:-28px;width:66px;height:66px;border-width:7px"></div>
  <div class="ring orange" style="left:98px;top:92px;width:66px;height:66px;border-width:7px"></div>
  <div class="icon" style="left:28px;top:59px;width:16px;height:16px"></div>
  <div class="label" style="left:26px;top:78px">PAYMENT</div>
  <p class="body" style="left:19px;top:82px;width:36px;text-align:center">Card data typed at every checkout step</p>
  <div class="icon" style="left:72px;top:59px;width:16px;height:16px"></div>
  <div class="label" style="left:70px;top:78px">PAYMENT</div>
  <p class="body" style="left:63px;top:82px;width:36px;text-align:center">Fraud rules decline good customers</p>
  <div class="foot">Lumivanta <span class="num">04</span></div>
</section>

<section class="slide small" style="left:42px;top:604px">
  <div class="ring orange" style="left:-36px;top:-40px;width:70px;height:70px;border-width:7px"></div>
  <div class="ring purple" style="left:-36px;top:88px;width:70px;height:70px;border-width:7px"></div>
  <div class="photo mono" style="left:14px;top:21px;width:86px;height:78px" role="img" aria-label="Photo of a phone showing a mobile wallet next to a payment card"></div>
  <div class="sq purple" style="left:204px;top:3px;width:7px;height:7px"></div>
  <div class="title-light" style="left:113px;top:17px;font-size:11px">Market<br>challenges</div>
  <p class="body" style="left:113px;top:42px;width:82px">Card fraud keeps rising online while strong checks add friction. Merchants lose sales at the final step and issuers lose approvals to false declines.</p>
  <p class="body" style="left:113px;top:60px;width:82px">Legacy processors are slow to add virtual cards, digital ID and passwordless sign in across regional markets.</p>
  <div class="icon" style="left:115px;top:86px;width:10px;height:10px"></div>
  <div class="label" style="left:128px;top:86px">PAYMENT</div>
  <p class="body" style="left:128px;top:90px;width:68px">Abandoned carts cost online stores heavy revenue each year.</p>
  <div class="foot">Lumivanta <span class="num">05</span></div>
</section>

<section class="slide small" style="left:273px;top:604px">
  <div class="sq purple" style="left:3px;top:3px;width:7px;height:7px"></div>
  <div class="title-light" style="left:13px;top:16px;font-size:10.5px">Market<br>opportunities</div>
  <p class="body" style="left:13px;top:40px;width:90px">Virtual cards, second factor checks and digital ID are growing fast as regional banks and fintechs move card services to the cloud.</p>
  <p class="body" style="left:13px;top:58px;width:90px">Higher approval rates and fewer abandoned carts give a clear, measurable return for every merchant we serve.</p>
  <div class="label" style="left:28px;top:82px;font-size:2px;color:var(--purple)">VIRTUAL CARDS</div>
  <div class="label" style="left:56px;top:82px;font-size:2px;color:var(--purple)">DIGITAL ID</div>
  <svg class="abs" style="left:24px;top:85px" width="60" height="24" viewBox="0 0 60 24">
    <circle cx="12" cy="12" r="10" fill="none" stroke="#f1e3ef" stroke-width="1.4"/>
    <circle cx="12" cy="12" r="10" fill="none" stroke="#7e2d86" stroke-width="1.4" stroke-dasharray="42 63" transform="rotate(-90 12 12)"/>
    <text x="12" y="13.5" font-size="4" text-anchor="middle" fill="#ee8a2a" font-family="Poppins">4356</text>
    <circle cx="40" cy="12" r="10" fill="none" stroke="#f1e3ef" stroke-width="1.4"/>
    <circle cx="40" cy="12" r="10" fill="none" stroke="#7e2d86" stroke-width="1.4" stroke-dasharray="30 63" transform="rotate(-90 40 12)"/>
    <text x="40" y="13.5" font-size="4" text-anchor="middle" fill="#ee8a2a" font-family="Poppins">2164</text>
  </svg>
  <svg class="abs" style="left:117px;top:17px" width="72" height="44" viewBox="0 0 72 44">
    <g stroke="#e4e4e4" stroke-width=".3">
      <line x1="4" y1="2" x2="4" y2="40"/><line x1="4" y1="40" x2="70" y2="40"/>
      <line x1="4" y1="10" x2="70" y2="10"/><line x1="4" y1="20" x2="70" y2="20"/><line x1="4" y1="30" x2="70" y2="30"/>
    </g>
    <rect x="22" y="2" width="14" height="4" fill="#f2a743"/>
    <text x="29" y="5" font-size="2" text-anchor="middle" fill="#fff" font-family="Poppins">Title value</text>
    <path d="M4 38 C14 10 24 8 34 12 S52 24 66 6" fill="none" stroke="#ee8a2a" stroke-width=".7"/>
    <path d="M4 36 C16 18 26 14 38 18 S54 8 66 10" fill="none" stroke="#a7469a" stroke-width=".7"/>
    <path d="M4 38 C16 24 28 20 40 24 S56 18 66 16" fill="none" stroke="#f2a743" stroke-width=".7"/>
    <path d="M4 39 C18 30 30 28 42 30 S58 26 66 28" fill="none" stroke="#7e2d86" stroke-width=".7"/>
    <g fill="#7e2d86"><circle cx="34" cy="12" r=".9"/><circle cx="66" cy="6" r=".9"/><circle cx="66" cy="16" r=".9"/><circle cx="40" cy="24" r=".9"/></g>
  </svg>
  <svg class="abs" style="left:112px;top:62px" width="88" height="42" viewBox="0 0 88 42">
    <g font-size="2" fill="#999" font-family="Open Sans"><text x="0" y="4">600</text><text x="0" y="12">450</text><text x="0" y="20">300</text><text x="0" y="28">150</text><text x="0" y="38">0</text></g>
    <path d="M8 38 C12 20 16 30 20 30 C26 30 28 26 32 22 C38 14 40 30 44 28 C50 24 50 4 56 6 C62 8 62 30 68 32 C74 34 76 30 84 36 L84 38 Z" fill="#ee8a2a"/>
    <g font-size="2.6" fill="#7e2d86" font-family="Poppins" font-style="italic"><text x="10" y="18">100</text><text x="18" y="28">20</text><text x="32" y="12">275</text><text x="44" y="22">130</text><text x="55" y="4">650</text><text x="74" y="28">80</text></g>
  </svg>
  <div class="foot">Lumivanta <span class="num">06</span></div>
</section>

<section class="slide small" style="left:505px;top:604px">
  <div class="sq purple" style="left:0;top:18px;width:10px;height:22px"></div>
  <div class="sq orange" style="left:204px;top:3px;width:8px;height:8px"></div>
  <div class="title-light" style="left:17px;top:16px;font-size:7px">Product<br>features and<br><b style="font-weight:700">functionality</b></div>
  <p class="body" style="left:17px;top:42px;width:68px">API based issuing, acquiring and fraud checks on one cloud platform, ready for banks, fintechs and merchants.</p>
  <p class="body" style="left:17px;top:58px;width:68px">Apps give shoppers dynamic virtual cards, 2FA and passwordless sign in at checkout.</p>
  <p class="body" style="left:17px;top:72px;width:68px">Each module can be added alone or as a full stack as clients grow.</p>
  <svg class="abs" style="left:100px;top:14px" width="112" height="62" viewBox="0 0 112 62">
    <g stroke="#7e2d86" stroke-width=".8"><line x1="54" y1="45" x2="42" y2="16"/><line x1="54" y1="45" x2="66" y2="16"/><line x1="54" y1="45" x2="27" y2="33"/><line x1="54" y1="45" x2="81" y2="33"/></g>
    <circle cx="54" cy="45" r="14" fill="#ee8a2a" stroke="#fff" stroke-width="1.5" stroke-dasharray="2 1.5"/>
    <circle cx="54" cy="45" r="10" fill="#ee8a2a"/>
    <text x="54" y="46.5" font-size="3.6" text-anchor="middle" fill="#fff" font-family="Poppins" font-weight="700">Lumivanta</text>
    <g fill="#7e2d86"><circle cx="42" cy="13" r="6"/><circle cx="66" cy="13" r="6"/><circle cx="27" cy="32" r="6"/><circle cx="81" cy="32" r="6"/></g>
    <g font-size="1.8" fill="#fff" text-anchor="middle" font-family="Poppins"><text x="42" y="17">Option B</text><text x="66" y="17">Option C</text><text x="27" y="36">Option A</text><text x="81" y="36">Option D</text></g>
    <g font-size="2" fill="#ee8a2a" font-family="Poppins"><text x="30" y="4">Your Title</text><text x="78" y="4">Your Title</text><text x="2" y="22">Your Title</text><text x="92" y="22">Your Title</text></g>
  </svg>
  <div class="icon" style="left:102px;top:75px;width:10px;height:10px"></div>
  <div class="label" style="left:116px;top:75px">PAYMENT</div>
  <p class="body" style="left:116px;top:79px;width:80px">Tokenised virtual cards for each online purchase.</p>
  <div class="icon" style="left:102px;top:92px;width:10px;height:10px"></div>
  <div class="label" style="left:116px;top:92px">PAYMENT</div>
  <p class="body" style="left:116px;top:96px;width:80px">Passwordless sign in backed by digital ID.</p>
  <div class="ring purple" style="left:-10px;top:104px;width:32px;height:32px;border-width:4px"></div>
  <div class="foot">Lumivanta <span class="num">07</span></div>
</section>

<section class="slide small" style="left:42px;top:739px">
  <div class="sq purple" style="left:3px;top:3px;width:5px;height:5px"></div>
  <div class="ring orange" style="left:184px;top:-22px;width:48px;height:48px;border-width:6px"></div>
  <div class="ring orange" style="left:-18px;top:68px;width:44px;height:44px;border-width:6px"></div>
  <div class="ring purple" style="left:-12px;top:96px;width:40px;height:40px;border-width:5px"></div>
  <div class="ring orange" style="left:90px;top:35px;width:24px;height:24px;border-width:3px"></div>
  <svg class="abs" style="left:14px;top:8px" width="100" height="100" viewBox="0 0 100 100">
    <g fill="#fff" stroke="#222" stroke-width="1"><rect x="3" y="2" width="24" height="48" rx="3"/><rect x="35" y="26" width="24" height="47" rx="3"/><rect x="67" y="44" width="24" height="50" rx="3"/></g>
    <g fill="#222"><rect x="11" y="2" width="8" height="1.6" rx=".8"/><rect x="43" y="26" width="8" height="1.6" rx=".8"/><rect x="75" y="44" width="8" height="1.6" rx=".8"/></g>
    <g font-family="Poppins" fill="#7e2d86" font-size="3.2"><text x="6" y="11">Card</text><text x="6" y="15">issuing</text><text x="38" y="35">Online</text><text x="38" y="39">checkout</text><text x="70" y="53">Digital ID</text></g>
    <g fill="none" stroke="#ee8a2a" stroke-width=".5"><rect x="12" y="21" width="6" height="4"/><circle cx="47" cy="48" r="2.5"/><rect x="76" y="63" width="6" height="5"/></g>
    <g font-family="Open Sans" fill="#999" font-size="1.7"><text x="6" y="32">Issue cards in</text><text x="6" y="34.5">minutes by API</text><text x="38" y="58">Fewer steps at</text><text x="38" y="60.5">the point of sale</text><text x="70" y="78">Sign in with no</text><text x="70" y="80.5">password needed</text></g>
  </svg>
  <div class="title-light" style="left:124px;top:27px;font-size:11px">Use cases</div>
  <p class="body" style="left:124px;top:41px;width:78px">A regional bank issues virtual cards through our API and lifts online approvals. A retailer adds one tap checkout and sees fewer abandoned carts.</p>
  <p class="body" style="left:124px;top:61px;width:78px">A transport fintech uses passwordless sign in and digital ID to onboard riders without passwords or codes.</p>
  <div class="foot">Lumivanta <span class="num">08</span></div>
</section>

<section class="slide small" style="left:273px;top:739px">
  <svg class="abs" style="left:0;top:0" width="62" height="121" viewBox="0 0 62 121">
    <path d="M0 1 A60 60 0 0 1 35.3 12.5 L17.6 36.7 A30 30 0 0 0 0 31 Z" fill="#7e2d86"/>
    <path d="M35.3 12.5 A60 60 0 0 1 57.1 42.5 L28.5 51.7 A30 30 0 0 0 17.6 36.7 Z" fill="#ee8a2a"/>
    <path d="M57.1 42.5 A60 60 0 0 1 57.1 79.5 L28.5 70.3 A30 30 0 0 0 28.5 51.7 Z" fill="#7e2d86"/>
    <path d="M57.1 79.5 A60 60 0 0 1 35.3 109.5 L17.6 85.3 A30 30 0 0 0 28.5 70.3 Z" fill="#ee8a2a"/>
    <path d="M35.3 109.5 A60 60 0 0 1 0 121 L0 91 A30 30 0 0 0 17.6 85.3 Z" fill="#7e2d86"/>
    <g fill="none" stroke="#fff" stroke-width=".8"><circle cx="10" cy="14" r="3"/><rect x="36" y="27" width="6" height="5"/><circle cx="46" cy="61" r="3.5"/><rect x="36" y="89" width="6" height="5"/><circle cx="10" cy="108" r="3"/></g>
    <text transform="translate(12 61) rotate(-90)" font-size="6.5" font-weight="700" text-anchor="middle" fill="#7e2d86" font-family="Poppins">Lumivanta</text>
  </svg>
  <div class="ring purple" style="left:195px;top:-18px;width:32px;height:32px;border-width:4px"></div>
  <div class="title-light" style="left:79px;top:12px;font-size:9.5px">Financial<br>spend and funding</div>
  <p class="body" style="left:79px;top:35px;width:126px">We plan to raise seed capital to scale our QMO cloud platform, grow sales across regional markets and secure new card scheme licences.</p>
  <p class="body" style="left:79px;top:45px;width:126px">Spend over the next two years is split across product build, sales, compliance and operations, with clear milestones for each round.</p>
  <div class="icon" style="left:78px;top:64px;width:7px;height:7px"></div>
  <div class="label" style="left:88px;top:63px;color:var(--purple);font-size:3px">TITLE</div>
  <p class="body" style="left:88px;top:66px;width:46px">Product build and platform growth</p>
  <div class="icon" style="left:140px;top:64px;width:7px;height:7px"></div>
  <div class="label" style="left:150px;top:63px;color:var(--purple);font-size:3px">TITLE</div>
  <p class="body" style="left:150px;top:66px;width:46px">Sales team for target regions</p>
  <div class="icon" style="left:78px;top:86px;width:7px;height:7px"></div>
  <div class="label" style="left:88px;top:85px;color:var(--purple);font-size:3px">TITLE</div>
  <p class="body" style="left:88px;top:88px;width:46px">Compliance, licences and security audits</p>
  <div class="icon" style="left:140px;top:86px;width:7px;height:7px"></div>
  <div class="label" style="left:150px;top:85px;color:var(--purple);font-size:3px">TITLE</div>
  <p class="body" style="left:150px;top:88px;width:46px">Operations and customer support</p>
  <div class="foot">Lumivanta <span class="num">09</span></div>
</section>

<section class="slide small" style="left:505px;top:739px">
  <div class="title-light" style="left:15px;top:8px;font-size:8px">Team members<br>and advisors</div>
  <div class="ring purple" style="left:190px;top:-12px;width:28px;height:28px;border-width:3px"></div>
  <div class="ring orange" style="left:-12px;top:98px;width:34px;height:34px;border-width:4px"></div>
  <div class="avatar" role="img" aria-label="Portrait photo of team member" style="left:24px;top:35px"></div>
  <div class="label" style="left:18px;top:47px;font-size:2.3px;color:var(--purple)">TARIQ NOOR</div>
  <div class="label" style="left:44px;top:34px;font-size:3px;color:var(--ink)">CEO</div>
  <p class="body" style="left:44px;top:37px;width:36px;font-size:2px;line-height:2.8px">Twenty years in card issuing and payment processing across the region.</p>
  <div class="avatar" role="img" aria-label="Portrait photo of team member" style="left:24px;top:60px"></div>
  <div class="label" style="left:16px;top:72px;font-size:2.3px;color:var(--purple)">ELENA BRANDT</div>
  <div class="label" style="left:44px;top:59px;font-size:3px;color:var(--ink)">CTO</div>
  <p class="body" style="left:44px;top:62px;width:36px;font-size:2px;line-height:2.8px">Builds secure cloud APIs for fraud checks and digital identity.</p>
  <div class="avatar" role="img" aria-label="Portrait photo of team member" style="left:24px;top:84px"></div>
  <div class="label" style="left:18px;top:96px;font-size:2.3px;color:var(--purple)">PRIYA OSEI</div>
  <div class="label" style="left:44px;top:83px;font-size:3px;color:var(--ink)">ADVISOR</div>
  <p class="body" style="left:44px;top:86px;width:36px;font-size:2px;line-height:2.8px">Former bank executive guiding issuer and merchant partnerships.</p>
  <svg class="abs" style="left:95px;top:20px" width="115" height="80" viewBox="0 0 115 80">
    <g stroke="#bbb" stroke-width=".4" fill="none"><path d="M45 40 L40 14 L70 8"/><path d="M45 40 L72 40 L78 55"/><path d="M45 40 L20 52"/><path d="M45 40 L36 72"/></g>
  </svg>
  <div class="org p" role="img" aria-label="Illustrated advisor portrait" style="left:132px;top:26px;width:13px;height:13px"></div>
  <div class="org o" role="img" aria-label="Illustrated advisor portrait" style="left:164px;top:20px;width:13px;height:13px"></div>
  <div class="org p" role="img" aria-label="Illustrated lead team member portrait" style="left:133px;top:50px;width:20px;height:20px"></div>
  <div class="org o" role="img" aria-label="Illustrated advisor portrait" style="left:165px;top:58px;width:13px;height:13px"></div>
  <div class="org p" role="img" aria-label="Illustrated advisor portrait" style="left:186px;top:79px;width:12px;height:12px"></div>
  <div class="org p" role="img" aria-label="Illustrated advisor portrait" style="left:99px;top:67px;width:13px;height:13px"></div>
  <div class="org o" role="img" aria-label="Illustrated advisor portrait" style="left:127px;top:84px;width:12px;height:12px"></div>
  <div class="letter" style="left:157px;top:19px">B</div>
  <div class="letter" style="left:140px;top:44px">A</div>
  <div class="letter" style="left:177px;top:64px">C</div>
  <div class="letter" style="left:194px;top:72px">D</div>
  <div class="letter" style="left:134px;top:77px">E</div>
  <div class="letter" style="left:110px;top:81px">F</div>
  <div class="foot">Lumivanta <span class="num">10</span></div>
</section>

<section class="slide small" style="left:42px;top:874px">
  <div class="ring purple" style="left:175px;top:-8px;width:50px;height:50px;border-width:5px"></div>
  <div class="ring orange" style="left:183px;top:10px;width:36px;height:36px;border-width:4px"></div>
  <div class="road-art" role="img" aria-label="3D illustration of a winding purple road with numbered orange milestone markers"></div>
  <div class="label" style="left:8px;top:22px;font-size:4.5px">+3467</div>
  <p class="body" style="left:8px;top:28px;color:var(--purple);font-style:italic;font-weight:600">Live merchants<br>onboarded to date</p>
  <div class="opt" style="left:94px;top:20px">OPTION<span>Launch issuing API</span></div>
  <div class="opt" style="left:124px;top:37px">OPTION<span>Add 2FA and digital ID</span></div>
  <div class="opt" style="left:148px;top:56px">OPTION<span>Expand to airlines</span></div>
  <div class="title-light" style="left:8px;top:54px;font-size:5.5px">Timeline of</div>
  <div class="title-bold" style="left:8px;top:60px;font-size:9.5px;font-weight:600">Roadmap</div>
  <div class="label" style="left:8px;top:71px;font-size:4px">FOR 2 YEARS</div>
  <div class="icon" style="left:8px;top:84px;width:10px;height:10px;border:none;box-shadow:none"></div>
  <div class="abs" style="left:10.5px;top:84.5px;font-weight:700;font-size:6px;color:var(--white)">A</div>
  <div class="label" style="left:21px;top:83px;font-size:5px;color:var(--purple)">Y1</div>
  <p class="body" style="left:21px;top:89px;font-size:1.9px;line-height:2.6px">Platform launch,<br>first bank clients</p>
  <div class="icon" style="left:55px;top:84px;width:10px;height:10px;border:none;box-shadow:none"></div>
  <div class="abs" style="left:57.5px;top:84.5px;font-weight:700;font-size:6px;color:var(--white)">B</div>
  <div class="label" style="left:68px;top:83px;font-size:5px;color:var(--purple)">Y2</div>
  <p class="body" style="left:68px;top:89px;font-size:1.9px;line-height:2.6px">Regional scale,<br>new verticals</p>
  <div class="foot">Lumivanta <span class="num">11</span></div>
</section>

<section class="slide small" style="left:273px;top:874px">
  <div class="ring orange" style="left:155px;top:-30px;width:56px;height:56px;border-width:6px"></div>
  <div class="ring purple" style="left:-14px;top:100px;width:44px;height:44px;border-width:5px"></div>
  <div class="sq purple" style="left:145px;top:20px;width:55px;height:72px"></div>
  <div class="photo cool" style="left:117px;top:25px;width:78px;height:71px" role="img" aria-label="Photo of a hand paying online with a smartphone"></div>
  <div class="title-light" style="left:22px;top:14px;font-size:9.5px">Competitive</div>
  <div class="title-bold" style="left:22px;top:24px;font-size:9.5px">Advantage<br>and USP</div>
  <p class="body" style="left:22px;top:46px;width:80px">One cloud stack covers issuing, acquiring, fraud checks and digital ID, so clients avoid stitching many vendors together.</p>
  <p class="body" style="left:22px;top:62px;width:80px">Dynamic virtual cards and passwordless sign in lift approvals while cutting fraud at checkout.</p>
  <p class="body" style="left:22px;top:76px;width:80px">Fast API onboarding lets banks and fintechs go live in weeks, not months.</p>
  <div class="foot">Lumivanta <span class="num">12</span></div>
</section>

<section class="slide small" style="left:505px;top:874px">
  <div class="ring orange" style="left:194px;top:-14px;width:28px;height:28px;border-width:3px"></div>
  <div class="title-light" style="left:12px;top:11px;font-size:8px;letter-spacing:-.1px">Business solutions &amp; client verticals</div>
  <div class="label" style="left:12px;top:26px;font-weight:400">Target Client Verticals</div>
  <p class="body" style="left:13px;top:32px;font-size:3px;line-height:4.2px;color:#666">• Financial Institutions<br>&nbsp;&nbsp;&nbsp;• Issuers<br>&nbsp;&nbsp;&nbsp;• Acquirers<br>&nbsp;&nbsp;&nbsp;• Banks<br>&nbsp;&nbsp;&nbsp;• FinTechs<br>• Airlines<br>• Hotels<br>• Merchant Aggregators<br>• Large Retailers<br>• SMEs</p>
  <table class="grid-table">
    <tr><td>ISSUING</td><td>CARDS</td><td>ACQUIRING</td><td>ECOMMERCE</td><td>SCHEMES</td></tr>
    <tr><td>Debit</td><td>BIN</td><td>Merchant</td><td>Gateway</td><td></td></tr>
    <tr><td>Prepaid</td><td>Virtual</td><td>POS</td><td>Tokens</td><td></td></tr>
    <tr><td>Credit</td><td>Fleet</td><td>Settlement</td><td>Wallet</td><td></td></tr>
    <tr><td>Fuel</td><td>Travel</td><td>Reports</td><td>Risk</td><td></td></tr>
  </table>
  <div class="sq" style="left:192px;top:33px;width:6px;height:4px;background:#bbb"></div>
  <div class="sq" style="left:192px;top:40px;width:6px;height:4px;background:#bbb"></div>
  <div class="sq" style="left:192px;top:47px;width:6px;height:4px;background:#bbb"></div>
  <div class="sq purple" style="left:120px;top:26px;width:5px;height:31px"></div>
  <div class="sq purple" style="left:126px;top:58px;width:63px;height:4px"></div>
  <div class="sq purple" style="left:126px;top:63px;width:63px;height:4px"></div>
  <div class="sq purple" style="left:126px;top:68px;width:63px;height:4px"></div>
  <div class="sq purple" style="left:201px;top:26px;width:4px;height:40px"></div>
  <div class="sq purple" style="left:207px;top:26px;width:4px;height:40px"></div>
  <div class="solutions-band">
    <b>BUSINESS SOLUTIONS</b>
    Digital Payment Processing, Fraud Prevention, Corporate Cards, Keyless Entry, Loyalty,<br>Single ID Management, Travel Cards, Fleet &amp; Fuel Cards, OTP/2FA<br>Passwordless Login, Enhanced Identity Verification
  </div>
  <div class="foot">Lumivanta <span class="num">13</span></div>
</section>

<section class="slide small" style="left:42px;top:1010px">
  <div class="eco-head">LUMIVANTA PAYMENT ECOSYSTEM</div>
  <div class="ring orange" style="left:-14px;top:92px;width:32px;height:32px;border-width:4px"></div>
  <div class="ring purple" style="left:-10px;top:100px;width:22px;height:22px;border-width:2px"></div>
  <div class="eco-art" role="img" aria-label="Technical diagram of the payment ecosystem linking acquirers, the payment network cloud, the central platform and client institutions"></div>
  <div class="foot">Lumivanta <span class="num">14</span></div>
</section>

<section class="slide small" style="left:273px;top:1010px">
  <div class="ring orange" style="left:10px;top:-32px;width:44px;height:44px;border-width:5px"></div>
  <div class="ring purple" style="left:-8px;top:100px;width:36px;height:36px;border-width:5px"></div>
  <div class="abs" style="left:148px;top:22px;width:58px;height:58px;border-radius:50%;background:var(--orange)"></div>
  <div class="sq purple" style="left:135px;top:21px;width:56px;height:84px"></div>
  <div class="photo cool" style="left:131px;top:25px;width:56px;height:80px" role="img" aria-label="Photo of a phone held over a card payment terminal"></div>
  <div class="title-light" style="left:11px;top:33px;font-size:9.3px">Benefits to each</div>
  <div class="title-light" style="left:11px;top:43px;font-size:9.3px;color:var(--orange);font-weight:400">Customer segments</div>
  <p class="body" style="left:11px;top:55px;width:112px">Banks and issuers raise approval rates and cut fraud losses with virtual cards and strong customer checks.</p>
  <p class="body" style="left:11px;top:67px;width:112px">Merchants recover abandoned carts with fast, secure checkout and fewer declined orders online.</p>
  <p class="body" style="left:11px;top:79px;width:112px">Fintechs and transport firms launch cards and digital ID quickly through one simple API.</p>
  <div class="foot">Lumivanta <span class="num">15</span></div>
</section>

<section class="slide small" style="left:505px;top:1010px">
  <div class="photo mono-light" style="left:80px;top:0;width:135px;height:121px" role="img" aria-label="Black and white photo of a person shopping online with a card and laptop"></div>
  <div class="ring purple" style="left:-22px;top:-24px;width:54px;height:54px;border-width:6px"></div>
  <div class="ring orange" style="left:58px;top:94px;width:52px;height:52px;border-width:6px;opacity:.92"></div>
  <div class="sq purple" style="left:196px;top:12px;width:10px;height:10px"></div>
  <div class="abs" style="left:35px;top:43px;width:91px;height:34px;background:var(--white)"></div>
  <div class="sq purple" style="left:35px;top:43px;width:8px;height:34px"></div>
  <div class="abs" style="left:51px;top:47px;font-weight:600;font-size:11px;color:var(--orange)">Thank You</div>
  <p class="abs" style="left:51px;top:63px;font-family:'Open Sans',sans-serif;font-size:2.9px;line-height:3.6px;color:var(--orange)"><span style="color:#d7731f">online payment security</span><br>to eliminate cart abandonment</p>
  <div class="abs" style="left:9px;top:110px;font-size:3.5px;letter-spacing:1.3px;color:var(--purple)">lumivanta.io</div>
</section>

</body>
</html>
```